Bed & Breakfast Business Card Design

Casa Mirador Bed & Breakfast is a private, adult-only, upscale retreat for guests vacationing or on business in the Atlanta area.

Event venue for weddings & retreats

Target Market(s)

Age 40+ couples, romantic get-aways, honeymoon, small weddings, business retreats

Industry/Entity Type

Business

Contact Information for Business Card

Casa Mirador Bed & Breakfast, LLC
7208 Bramwick Ferry Road
Larkhollow, GA 30999
555-555-0193
www.CasaMiradorRetreat-example.com

```html
<!DOCTYPE html>
<html lang="en">
<head>
<meta charset="utf-8">
<title>Casa Mirador Bed &amp; Breakfast – Business Card</title>
<link href="https://fonts.googleapis.com/css2?family=Dancing+Script:wght@500;700&family=Open+Sans:wght@700;800&display=swap" rel="stylesheet">
<style>
  :root {
    --backdrop: #e9e4dd;
    --peach-light: #f8cfa3;
    --peach-mid: #f2b27c;
    --peach-deep: #e89a62;
    --ink: #3c3a38;
    --star-blue: #3f88b8;
    --banner-navy: #34466d;
    --banner-text: #ffffff;
    --sky-night: #23355e;
    --sky-dusk: #5a6f9a;
    --stucco: #b88a5c;
    --interior-warm: #9a5a3a;
    --interior-light: #e2c49a;
  }
  * { box-sizing: border-box; margin: 0; padding: 0; }
  html, body { width: 1200px; height: 723px; overflow: hidden; }
  body {
    background: var(--backdrop);
    display: flex;
    align-items: center;
    justify-content: center;
    gap: 70px;
  }
  .card {
    width: 340px;
    height: 595px;
    box-shadow: 0 6px 18px rgba(0,0,0,.18);
    position: relative;
    overflow: hidden;
  }

  /* Back side */
  .card-back {
    background: radial-gradient(ellipse at 40% 35%, var(--peach-light), var(--peach-mid) 60%, var(--peach-deep));
    display: flex;
    flex-direction: column;
    align-items: center;
    justify-content: space-between;
    padding: 46px 16px 44px;
    text-align: center;
    color: var(--ink);
    font-family: 'Dancing Script', cursive;
  }
  .star-mark {
    width: 30px; height: 30px;
    background: var(--star-blue);
    transform: rotate(45deg);
  }
  .address { font-size: 30px; line-height: 1.15; font-weight: 500; }
  .phone { font-size: 34px; font-weight: 500; letter-spacing: 1px; }
  .website { font-size: 19px; font-weight: 500; white-space: nowrap; }

  /* Front side */
  .card-front { display: flex; flex-direction: column; }
  .photo-exterior {
    height: 160px;
    background: linear-gradient(180deg, var(--sky-night) 0%, var(--sky-dusk) 45%, var(--stucco) 100%);
  }
  .name-banner {
    height: 130px;
    background: var(--banner-navy);
    color: var(--banner-text);
    display: flex;
    flex-direction: column;
    align-items: center;
    justify-content: center;
  }
  .name-banner .business-name {
    font-family: 'Dancing Script', cursive;
    font-weight: 700;
    font-size: 46px;
    line-height: 1;
  }
  .name-banner .business-type {
    font-family: 'Open Sans', sans-serif;
    font-weight: 800;
    font-size: 30px;
    letter-spacing: 1px;
    margin-top: 8px;
  }
  .photo-interior {
    flex: 1;
    background: linear-gradient(160deg, var(--interior-light) 0%, var(--interior-warm) 55%, #6b3b2a 100%);
  }
</style>
</head>
<body>
  <section class="card card-back">
    <div class="star-mark" role="img" aria-label="Blue star ornament"></div>
    <p class="address">Bramwick Ferry Road<br>Larkhollow, GA<br>30999</p>
    <div class="star-mark" role="img" aria-label="Blue star ornament"></div>
    <p class="phone">555-555-0193</p>
    <div class="star-mark" role="img" aria-label="Blue star ornament"></div>
    <p class="website">www.CasaMiradorRetreat-example.com</p>
  </section>

  <section class="card card-front">
    <div class="photo-exterior" role="img" aria-label="Photo of the inn's arched stucco courtyard at dusk under a night sky"></div>
    <div class="name-banner">
      <span class="business-name">Casa Mirador</span>
      <span class="business-type">BED &amp; BREAKFAST</span>
    </div>
    <div class="photo-interior" role="img" aria-label="Photo of the warm, colourful dining room with wooden tables and chairs"></div>
  </section>
</body>
</html>
```